Brand Finder - show where popular alcoholic products are sold

We need a web design for a "Brand Finder" which shows a selection of alcohol products and where to buy these (with a Quorvin map of the surrounding area with markers on the map).

We have a functioning version, but we're not satisfied with the current user experience. We need to handle several scenarios based on the number of products (i.e. manufacturers with a few products, with dozens of products or even hundreds of products - each could have a varied design if it mattered).

This should also be compatible with standard required for a Plimbook app.

Our current example is at http://sipvelt.example/brandfinder/index.php?address=Atlanta%2C+GA&yt1= - go ahead and click on the Varnell Copperhollow product and you'll see something that looks like http://clipmorra.example/t/7kQ9WzxxLTe - this screen is really where we want to start (not the previous screen) and in fact we'll also want controls to do searching and filtering (search by name or keyword and filtering by product type such as rum, vodka, wine, beer, etc)

[REVISION] - I have now uploaded a SPEC document with some sketches. Please pay attention to the Plimbook/Website widgets (this is the design portion we are asking for here, not the mobile app - but the winner might get a second design opportunity for the mobile app afterwards.

Target Market(s)

drinkers looking to find out where to buy their favorite products.

Industry/Entity Type

Quorvin

Number of Pages Required

1 page

Requirements
Must have
• Method to select from among a number of products.
• It must be compatible with a Plimbook tab (Plimbook app).
Nice to have
• If we can even make use of multiple select (i.e. product #1 and #3, but not #2), then that would be good too.
• It will also integrate as a widget in other websites (e.g. the manufacturer's own website), so there should be a way to configure/change color scheme to match and integrate well into other websites as a widget.

```html
<!DOCTYPE html>
<html lang="en">
<head>
<meta charset="utf-8">
<title>Sipvelt Brand Finder</title>
<link rel="stylesheet" href="https://fonts.googleapis.com/css2?family=Source+Sans+3:ital,wght@0,400;0,600;0,700;1,400&display=swap">
<style>
  :root {
    --status-bg: #1e4a60;
    --ink: #111111;
    --panel: #eeeeee;
    --field-border: #9a9a9a;
    --placeholder: #8c8c8c;
    --accent: #0a8fe6;
    --muted: #9b9b9b;
    --body-text: #333333;
    --link: #1f86d6;
    --map-base: #e8e4da;
    --tile: #bde7e5;
    --tile-label: #1b8fa3;
    --legend-bg: #f7f7f7;
    --store-pin: #1a8de0;
    --bar-pin: #12a150;
    --white: #ffffff;
    --amber: #d59a2c;
  }
  * { box-sizing: border-box; margin: 0; padding: 0; }
  html, body { width: 675px; height: 1200px; overflow: hidden; background: var(--white); }
  body { font-family: "Source Sans 3", "Helvetica Neue", Arial, sans-serif; color: var(--body-text); }
  .screen { position: relative; width: 675px; height: 1200px; overflow: hidden; }

  .status-bar {
    position: absolute; left: 0; top: 0; width: 675px; height: 34px;
    background: var(--status-bg); color: var(--white); font-size: 20px;
  }
  .status-bar .carrier { position: absolute; left: 10px; top: 5px; letter-spacing: 0.3px; }
  .status-bar .clock { position: absolute; left: 0; right: 0; top: 5px; text-align: center; font-weight: 600; }
  .status-bar svg { position: absolute; }

  .brand { position: absolute; left: 50px; top: 66px; display: flex; align-items: center; gap: 8px; }
  .brand-name { font-size: 35px; font-weight: 700; color: var(--ink); letter-spacing: 0.3px; }
  .brand-mark { width: 22px; height: 22px; background: var(--amber); }

  .search-panel {
    position: absolute; left: 56px; top: 132px; width: 580px; height: 175px;
    background: var(--panel); border-radius: 8px;
  }
  .field {
    position: absolute; left: 38px; width: 326px; height: 49px;
    background: var(--white); border: 1.5px solid var(--field-border); border-radius: 8px;
    font-size: 21px; font-style: italic; color: var(--placeholder);
    padding: 9px 0 0 26px;
  }
  .field svg { position: absolute; right: 18px; top: 12px; }
  .field-location { top: 24px; }
  .field-product { top: 98px; }
  .submit-button {
    position: absolute; left: 389px; top: 25px; width: 155px; height: 118px;
    background: var(--accent); border-radius: 6px; color: var(--white);
    font-size: 22px; font-weight: 700; display: flex; align-items: center; justify-content: center;
  }

  .venue-name { position: absolute; left: 56px; top: 320px; font-size: 17px; font-weight: 700; color: var(--muted); }
  .venue-col { position: absolute; top: 355px; font-size: 12.5px; line-height: 18px; color: var(--body-text); }
  .venue-col.address { left: 57px; }
  .venue-col.contact { left: 265px; }
  .venue-col.hours { left: 464px; }
  .directions-link { position: absolute; left: 56px; top: 416px; font-size: 16px; color: var(--link); text-decoration: underline; }

  .map-area { position: absolute; left: 0; top: 459px; width: 675px; height: 689px; background: linear-gradient(160deg, #ebe7de, var(--map-base) 60%, #efe3d6); }
  .map-markers { position: absolute; left: 0; top: 459px; width: 675px; height: 689px; overflow: hidden; }
  .map-popup {
    position: absolute; left: 338px; top: 518px; width: 262px; height: 91px;
    background: var(--white); border: 1px solid #c9c9c9; box-shadow: 0 2px 6px rgba(0,0,0,0.15); text-align: center;
  }
  .map-popup::after {
    content: ""; position: absolute; left: 122px; bottom: -10px;
    border-left: 9px solid transparent; border-right: 9px solid transparent; border-top: 10px solid var(--white);
  }
  .popup-title { margin-top: 23px; font-size: 13.5px; font-weight: 700; color: var(--link); }
  .popup-address { margin-top: 7px; font-size: 11.5px; color: #666666; }
  .popup-close { position: absolute; right: 10px; top: 4px; font-size: 17px; color: #777777; }

  .product-tile {
    position: absolute; left: 554px; width: 90px; height: 81px;
    background: var(--tile); border-radius: 5px; overflow: hidden;
  }
  .product-art { position: absolute; left: 23px; top: 8px; width: 44px; height: 50px; border-radius: 4px; }
  .product-label { position: absolute; left: 0; right: 0; bottom: 2px; text-align: center; font-size: 14px; color: var(--tile-label); }
  .tile-beer { top: 797px; } .tile-beer .product-art { background: linear-gradient(90deg, #7aa040, #e7c35a); }
  .tile-rum { top: 887px; } .tile-rum .product-art { background: linear-gradient(90deg, #c9761c, #e9a24b); }
  .tile-vodka { top: 977px; } .tile-vodka .product-art { background: linear-gradient(90deg, #e6e6e6, #d8303a); }
  .tile-wine { top: 1067px; } .tile-wine .product-art { background: linear-gradient(90deg, #5c1420, #9c2a3a); }

  .legend-bar { position: absolute; left: 0; top: 1148px; width: 675px; height: 52px; background: var(--legend-bg); }
  .legend-item { position: absolute; top: 13px; display: flex; align-items: center; gap: 8px; font-size: 14px; color: #333333; }
  .legend-store { left: 410px; }
  .legend-bar-item { left: 482px; }
  .legend-more { position: absolute; left: 588px; top: 9px; }
</style>
</head>
<body>
<div class="screen">
  <header class="status-bar">
    <span class="carrier">●●●○○ Veltra-UK</span>
    <svg style="left:158px;top:9px" width="20" height="16" viewBox="0 0 20 16" aria-hidden="true">
      <path d="M10 15 L6.5 11 A5 5 0 0 1 13.5 11 Z" fill="#fff"/>
      <path d="M3.5 8 A9 9 0 0 1 16.5 8" stroke="#fff" stroke-width="2" fill="none"/>
      <path d="M0.8 5 A13 13 0 0 1 19.2 5" stroke="#fff" stroke-width="2" fill="none"/>
    </svg>
    <span class="clock">13:59</span>
    <svg style="left:594px;top:7px" width="12" height="20" viewBox="0 0 12 20" aria-hidden="true">
      <path d="M1 5 L11 14 L6 19 V1 L11 6 L1 15" stroke="#fff" stroke-width="1.6" fill="none"/>
    </svg>
    <svg style="left:620px;top:8px" width="44" height="18" viewBox="0 0 44 18" aria-hidden="true">
      <rect x="1" y="1" width="38" height="16" rx="3" stroke="#fff" stroke-width="1.6" fill="none"/>
      <rect x="3.5" y="3.5" width="24" height="11" rx="1.5" fill="#fff"/>
      <rect x="40" y="6" width="3" height="6" rx="1" fill="#fff"/>
    </svg>
  </header>

  <div class="brand">
    <span class="brand-name">Sipvelt</span>
    <span class="brand-mark"></span>
  </div>

  <section class="search-panel">
    <div class="field field-location">My location
      <svg width="32" height="32" viewBox="0 0 32 32" aria-hidden="true">
        <circle cx="12" cy="12" r="9" stroke="#888" stroke-width="2" fill="none"/>
        <path d="M19 19 L29 29" stroke="#888" stroke-width="3" stroke-linecap="round"/>
      </svg>
    </div>
    <div class="field field-product">Product finder
      <svg width="26" height="24" viewBox="0 0 26 24" aria-hidden="true">
        <path d="M2 8 L13 18 L24 8" stroke="#888" stroke-width="2" fill="none"/>
      </svg>
    </div>
    <div class="submit-button">Submit</div>
  </section>

  <h2 class="venue-name">Orchard Cellar</h2>
  <div class="venue-col address">BAR &amp; PUB INFORMATION<br>42 Larkspur Rd Ste B<br>Tamsen GA 30612 US</div>
  <div class="venue-col contact">Tel: 0198-765-432<br>E-mail: orchard@mailvo.example</div>
  <div class="venue-col hours">Opening hours:<br>Mon-Thru: 17.00-01.00<br>Fri, Set, Sun: 11.00-03.00</div>
  <span class="directions-link">Get Direction</span>

  <div class="map-area" role="img" aria-label="Quorvin street map of the Atlanta area"></div>

  <svg class="map-markers" viewBox="0 0 675 689" role="img" aria-label="Store and bar markers on the map">
    <defs>
      <symbol id="pin-store" viewBox="0 0 36 46">
        <path d="M18 45 C10 34 2 28 2 17 A16 16 0 0 1 34 17 C34 28 26 34 18 45 Z" fill="var(--store-pin)"/>
        <path d="M12 9 h3 v4 l1.5 2 v12 h-6 v-12 l1.5 -2 Z" fill="#fff"/>
        <path d="M20 7 h3 v5 l1.5 2 v13 h-6 v-13 l1.5 -2 Z" fill="#fff"/>
      </symbol>
      <symbol id="pin-bar" viewBox="0 0 36 46">
        <path d="M18 45 C10 34 2 28 2 17 A16 16 0 0 1 34 17 C34 28 26 34 18 45 Z" fill="var(--bar-pin)"/>
        <path d="M11.5 8 H24.5 L22 27 H14 Z" fill="none" stroke="#fff" stroke-width="2"/>
        <path d="M13 14 H23 L21.6 24 H14.4 Z" fill="#fff"/>
      </symbol>
    </defs>
    <g class="bar-markers">
      <use href="#pin-bar" x="128" y="105" width="36" height="46"/>
      <use href="#pin-bar" x="189" y="111" width="36" height="46"/>
      <use href="#pin-bar" x="-9" y="138" width="36" height="46"/>
      <use href="#pin-bar" x="88" y="156" width="36" height="46"/>
      <use href="#pin-bar" x="38" y="177" width="36" height="46"/>
      <use href="#pin-bar" x="221" y="159" width="36" height="46"/>
      <use href="#pin-bar" x="126" y="197" width="36" height="46"/>
      <use href="#pin-bar" x="182" y="235" width="36" height="46"/>
      <use href="#pin-bar" x="70" y="235" width="36" height="46"/>
      <use href="#pin-bar" x="257" y="231" width="36" height="46"/>
      <use href="#pin-bar" x="335" y="184" width="36" height="46"/>
      <use href="#pin-bar" x="449" y="178" width="36" height="46"/>
      <use href="#pin-bar" x="176" y="294" width="36" height="46"/>
      <use href="#pin-bar" x="401" y="287" width="36" height="46"/>
      <use href="#pin-bar" x="97" y="339" width="36" height="46"/>
      <use href="#pin-bar" x="-18" y="312" width="36" height="46"/>
      <use href="#pin-bar" x="293" y="394" width="36" height="46"/>
      <use href="#pin-bar" x="5" y="404" width="36" height="46"/>
      <use href="#pin-bar" x="82" y="471" width="36" height="46"/>
      <use href="#pin-bar" x="223" y="485" width="36" height="46"/>
    </g>
    <g class="store-markers">
      <use href="#pin-store" x="0" y="44" width="36" height="46"/>
      <use href="#pin-store" x="212" y="60" width="36" height="46"/>
      <use href="#pin-store" x="43" y="134" width="36" height="46"/>
      <use href="#pin-store" x="135" y="134" width="36" height="46"/>
      <use href="#pin-store" x="243" y="170" width="36" height="46"/>
      <use href="#pin-store" x="12" y="228" width="36" height="46"/>
      <use href="#pin-store" x="158" y="224" width="36" height="46"/>
      <use href="#pin-store" x="124" y="258" width="36" height="46"/>
      <use href="#pin-store" x="295" y="241" width="36" height="46"/>
      <use href="#pin-store" x="57" y="296" width="36" height="46"/>
      <use href="#pin-store" x="234" y="291" width="36" height="46"/>
      <use href="#pin-store" x="14" y="332" width="36" height="46"/>
      <use href="#pin-store" x="147" y="336" width="36" height="46"/>
      <use href="#pin-store" x="169" y="390" width="36" height="46"/>
      <use href="#pin-store" x="48" y="411" width="36" height="46"/>
    </g>
  </svg>

  <div class="map-popup">
    <span class="popup-close">×</span>
    <p class="popup-title">Orchard Cellar</p>
    <p class="popup-address">42 Larkspur Rd Ste B</p>
  </div>

  <div class="product-tile tile-beer"><div class="product-art" role="img" aria-label="Beer bottle and glass"></div><span class="product-label">Beer</span></div>
  <div class="product-tile tile-rum"><div class="product-art" role="img" aria-label="Rum bottle and glass"></div><span class="product-label">Rum</span></div>
  <div class="product-tile tile-vodka"><div class="product-art" role="img" aria-label="Vodka bottle and glass"></div><span class="product-label">Vodka</span></div>
  <div class="product-tile tile-wine"><div class="product-art" role="img" aria-label="Red wine bottle and glass"></div><span class="product-label">Red Wine</span></div>

  <footer class="legend-bar">
    <div class="legend-item legend-store">
      <svg width="18" height="24" viewBox="0 0 36 46" aria-hidden="true"><use href="#pin-store" width="36" height="46"/></svg>
      <span>Store</span>
    </div>
    <div class="legend-item legend-bar-item">
      <svg width="18" height="24" viewBox="0 0 36 46" aria-hidden="true"><use href="#pin-bar" width="36" height="46"/></svg>
      <span>Bar</span>
    </div>
    <svg class="legend-more" width="26" height="26" viewBox="0 0 26 26" aria-hidden="true">
      <circle cx="13" cy="13" r="12" stroke="#999" stroke-width="1.4" fill="none"/>
      <path d="M7.5 11 L13 16 L18.5 11" stroke="#999" stroke-width="1.6" fill="none"/>
    </svg>
  </footer>
</div>
</body>
</html>
```